Poster for a 100 y.o. Tennis Tournament

I would like a poster designed to promote our tennis tournament but I'd like to avoid some of the clichés like the shadow of a player serving. Just well styled text would be fine but some clever imagery would be a bonus.
Highlighting the fact our tournament has been running for over 100 years would be nice so a retro design would work. But that doesn't mean a modern design, for example a minimalist approach utilising the lines of a tennis court, wouldn't work.
Updates

Our tennis committee is now in the process of short listing and will provide an update within 48 hours.

Industry/Entity Type

Court

Requirements
Must have
• The poster must contain the following text at a minimum:
"Marbury Tennis Tournament"/"Since 1908"
"9 March - 11 March, 2013" or "9-11 March, 2013", etc
"www.marburytennis.com.au"

The poster must be reproducible in colour and black & white, or at least have an alternate for black & white.

The poster must be usable in both A3 and A4 sizes.
Nice to have
• The poster should contain the following text:
"Championship"
"Handicap"
"Seniors"
"Juniors"
Each above may be optionally succeeded by "Singles & Doubles", e.g. "Championship Singles & Doubles". It would actually be clearer if this additional text was used but would be repetitive, so alternate text "Singles & Doubles in all categories" might also be used. Alternatives for variety (with the first word the focus): "Championship Singles & Doubles", "Handicap Singles & Doubles", "Seniors 35+ & 50+", "Juniors 18&U, 14&U"

Ideally the poster will provision room for four to eight sponsors logos, preferably at the bottom, but failure to do this is not a show stopper.

The following text may also be used:
"Entries close February 24"
"Tollard Plate Weekend"

Attached is a photo of one of the old trophies. Utilisation of the curved style of the "Marbury Tennis Tournament" text would fit in with the history if the tournament.

The ability to reuse elements of the poster in a single page website used to promote the tournament would be an advantage (as it will provide consistency).

If you could have an image of a tennis ball that conveys the same energy as the clock/tyre image in the attached "Under the Glass Moon" poster, that would be cool. Or using split imagery of a wooden racquet and a modern racquet, but with some energy, would also be good. These are just ideas though and by no means essential.

I've also attached a photo of a t-shirt with a poster layout I thought looked good.

Some additional text that can be used:
"Brand new courts"
"Brindle Park, Oakhurst Tce, Marbury"
"Phone 0427 318 642"
"Prizes and Trophies"

```html
<!DOCTYPE html>
<html lang="en">
<head>
<meta charset="utf-8">
<title>Marbury Tennis Tournament</title>
<link href="https://fonts.googleapis.com/css2?family=Roboto+Condensed:wght@400;700&family=PT+Sans+Narrow:wght@400;700&family=Open+Sans:wght@400;700&display=swap" rel="stylesheet">
<style>
  :root {
    --green: #1e9a4c;
    --grey: #4a4a4a;
    --navy: #2b3990;
    --ink: #111111;
    --gold-light: #f2ea4a;
    --gold: #c9b21c;
    --olive: #8a7d12;
    --lime: #7fbf2a;
    --paper: #ffffff;
  }
  * { box-sizing: border-box; margin: 0; padding: 0; }
  html, body { width: 884px; height: 1200px; overflow: hidden; background: #ffffff; }
  .poster { position: relative; width: 884px; height: 1200px; overflow: hidden; background: var(--paper); }

  .hero-photo {
    position: absolute; left: 0; top: 200px; width: 884px; height: 900px;
    background:
      radial-gradient(circle at 230px 270px, #d8e83a 0 90px, rgba(216,232,58,0) 150px),
      radial-gradient(ellipse at 520px 240px, rgba(246,190,60,0.55) 0 120px, rgba(246,190,60,0) 260px),
      radial-gradient(ellipse at 180px 560px, rgba(90,130,200,0.35) 0 160px, rgba(90,130,200,0) 320px),
      linear-gradient(180deg, #ffffff 0%, #f3f1ea 45%, #ffffff 100%);
  }

  .event-name {
    position: absolute; left: 0; top: 36px; width: 884px; text-align: center;
    font-family: "Roboto Condensed", sans-serif; font-weight: 700; color: var(--green);
    font-size: 74px; line-height: 80px; letter-spacing: 2px; text-transform: uppercase;
  }
  .since {
    position: absolute; left: 0; top: 206px; width: 884px; text-align: center;
    font-family: "Roboto Condensed", sans-serif; font-weight: 400; font-size: 28px;
    color: var(--grey); letter-spacing: 7px; text-transform: uppercase;
  }

  .prize-burst { position: absolute; left: 530px; top: 362px; width: 312px; height: 312px; }
  .prize-text {
    position: absolute; left: 530px; top: 438px; width: 312px; text-align: center;
    font-family: "Roboto Condensed", sans-serif; font-weight: 700; font-size: 50px; line-height: 1.05;
    color: #ffffff; text-shadow: 2px 2px 3px rgba(0,0,0,0.55);
  }

  .date-band {
    position: absolute; left: 0; top: 606px; width: 520px; height: 56px;
    background: linear-gradient(90deg, var(--olive), var(--gold-light) 45%, var(--gold));
    border-radius: 0 28px 28px 0;
    font-family: "Roboto Condensed", sans-serif; font-weight: 700; font-size: 35px; color: var(--ink);
    padding-left: 50px; line-height: 56px;
  }
  .entries-band {
    position: absolute; left: 0; top: 666px; width: 410px; height: 48px;
    background: var(--navy); border-radius: 0 24px 24px 0;
    font-family: "Roboto Condensed", sans-serif; font-weight: 700; font-size: 26px; color: #ffffff;
    padding-left: 50px; line-height: 48px;
  }

  .trophy-photo {
    position: absolute; left: 546px; top: 654px; width: 276px; height: 300px;
    border: 4px solid #ffffff; border-radius: 18px;
    background: radial-gradient(ellipse at 50% 45%, #6f6a5a 0%, #2c2a24 55%, #14130f 100%);
    box-shadow: 0 2px 8px rgba(0,0,0,0.35);
  }

  .categories { position: absolute; left: 52px; top: 798px; list-style: none; font-family: "Roboto Condensed", sans-serif; }
  .categories li { height: 44px; line-height: 44px; color: var(--ink); font-size: 23px; white-space: nowrap; }
  .categories .name { color: var(--navy); font-weight: 700; font-size: 31px; }

  .weekend {
    position: absolute; left: 466px; top: 956px; width: 350px; text-align: right;
    font-family: "Roboto Condensed", sans-serif; font-weight: 700; font-size: 30px; color: var(--ink);
  }

  .contact { position: absolute; left: 0; top: 1006px; width: 818px; text-align: right; white-space: nowrap; }
  .contact .label { font-family: "PT Sans Narrow", sans-serif; font-weight: 700; font-size: 32px; color: var(--navy); }
  .contact .phone { font-family: "Open Sans", sans-serif; font-weight: 700; font-size: 48px; color: var(--ink); letter-spacing: -0.5px; }

  .footer-wave { position: absolute; left: 0; top: 1040px; width: 884px; height: 160px; }

  .venue {
    position: absolute; left: 54px; top: 1122px; font-style: normal;
    font-family: "Open Sans", sans-serif; font-size: 19px; line-height: 28px; color: var(--ink);
  }
  .site {
    position: absolute; left: 470px; top: 1143px; width: 372px; text-align: right;
    font-family: "Open Sans", sans-serif; font-weight: 700; font-size: 24px; color: var(--ink); letter-spacing: 0.5px;
  }
</style>
</head>
<body>
<main class="poster">
  <div class="hero-photo" role="img" aria-label="Blurred action photograph of a yellow tennis ball striking racquet strings, a player in a yellow shirt behind"></div>

  <h1 class="event-name">Marbury Tennis<br>Tournament</h1>
  <div class="since">Since 1908</div>

  <svg class="prize-burst" viewBox="0 0 312 312" aria-hidden="true">
    <defs>
      <radialGradient id="burstFill" cx="45%" cy="40%" r="65%">
        <stop offset="0" stop-color="#efe04a"/>
        <stop offset="0.6" stop-color="#b8a218"/>
        <stop offset="1" stop-color="#7d700e"/>
      </radialGradient>
    </defs>
    <polygon fill="url(#burstFill)" stroke="#ffffff" stroke-width="4"
      points="156,6 168,32 186,10 193,38 216,20 216,49 242,38 236,66 264,62 252,88 280,90 264,113 291,122 270,140 296,156 270,172 291,190 264,199 280,222 252,224 264,250 236,246 242,274 216,263 216,292 193,274 186,302 168,280 156,306 144,280 126,302 119,274 96,292 96,263 70,274 76,246 48,250 60,224 32,222 48,199 21,190 42,172 16,156 42,140 21,122 48,113 32,90 60,88 48,62 76,66 70,38 96,49 96,20 119,38 126,10 144,32"/>
  </svg>
  <div class="prize-text">Prizes<br>and<br>Trophies</div>

  <div class="date-band">9 March - 11 March, 2013</div>
  <div class="entries-band">Entries Close February 24</div>

  <div class="trophy-photo" role="img" aria-label="Photograph of an engraved antique silver tennis trophy cup"></div>

  <ul class="categories">
    <li><span class="name">Championship -</span> Singles &amp; Doubles</li>
    <li><span class="name">Handicap -</span> Singles &amp; Doubles</li>
    <li><span class="name">Seniors -</span> 35+ &amp; 50+</li>
    <li><span class="name">Juniors -</span>&nbsp; 18 &amp; U, 14 &amp; U</li>
  </ul>

  <div class="weekend">Tollard Plate Weekend</div>
  <div class="contact"><span class="label">Contact Us - </span><span class="phone">0427 318 642</span></div>

  <svg class="footer-wave" viewBox="0 0 884 160" preserveAspectRatio="none" aria-hidden="true">
    <defs>
      <linearGradient id="footGold" x1="0" y1="0" x2="1" y2="0">
        <stop offset="0" stop-color="#8f8214"/>
        <stop offset="0.35" stop-color="#f4ec52"/>
        <stop offset="0.7" stop-color="#d2bd22"/>
        <stop offset="1" stop-color="#9c8b16"/>
      </linearGradient>
    </defs>
    <path d="M0,20 C180,-10 300,60 480,62 C650,64 760,30 884,40 L884,160 L0,160 Z" fill="#7fbf2a"/>
    <path d="M0,42 C180,18 300,86 480,86 C650,86 770,52 884,60 L884,160 L0,160 Z" fill="#ffffff"/>
    <path d="M0,54 C180,34 300,100 480,100 C650,100 770,66 884,72 L884,160 L0,160 Z" fill="url(#footGold)"/>
  </svg>

  <address class="venue">Brand new courts,<br>Brindle Park, Oakhurst Tce, Marbury.</address>
  <div class="site">www.marburytennis.com.au</div>
</main>
</body>
</html>
```